Eastfield Commercial Card

I would like a modern, eye catching card based off my logo design.
Info to include:
Anders Voll (Card Name)
eastfieldcommercial.example (Website)
555 203 8841 (Office/fax)
555 287 3096 (Business Cell)
anders@eastfieldcommercial.example (Work email)

Target Market(s)

Commercial real estate brokers, property owners.

Colors
ec1f27
757575

Requirements
Must have
• Name and info above. Not be lame!:)

```html
<!DOCTYPE html>
<html lang="en">
<head>
<meta charset="utf-8">
<title>Eastfield Commercial Card</title>
<link rel="stylesheet" href="https://fonts.googleapis.com/css2?family=Montserrat:wght@600;700&family=Lato:wght@400;700&display=swap">
<style>
  :root {
    --stage: #1e1e1f;
    --card-dark: #3d3d40;
    --card-back: #38383a;
    --paper: #ffffff;
    --brand-red: #a3161c;
    --ink-light: #f2f2f2;
    --ink-soft: #d6d6d8;
  }
  * { box-sizing: border-box; margin: 0; padding: 0; }
  html, body { width: 1200px; height: 930px; overflow: hidden; background: var(--stage); }
  .canvas { position: relative; width: 1200px; height: 930px; }

  .card {
    position: absolute;
    width: 540px; height: 310px;
    border-radius: 16px;
    overflow: hidden;
    box-shadow: 0 18px 40px rgba(0,0,0,.45);
  }

  /* back side */
  .card-back { left: 70px; top: 120px; background: var(--card-back); }
  .card-back .wordmark {
    position: absolute; left: 0; right: 0; top: 126px;
    text-align: center;
    font-family: "Montserrat", sans-serif; font-weight: 700;
    font-size: 30px; letter-spacing: .5px; text-transform: uppercase;
    color: var(--ink-light);
  }
  .card-back .site {
    position: absolute; left: 0; right: 0; bottom: 34px;
    text-align: center;
    font-family: "Lato", sans-serif; font-size: 14px; letter-spacing: .3px;
    color: var(--ink-soft);
  }

  /* front side */
  .card-front { left: 590px; top: 500px; background: var(--paper); }
  .card-front .shape { position: absolute; inset: 0; }
  .card-front .wordmark {
    position: absolute; right: 24px; top: 52px;
    font-family: "Montserrat", sans-serif; font-weight: 700;
    font-size: 19px; text-transform: uppercase; letter-spacing: .2px;
    color: var(--brand-red);
    white-space: nowrap;
  }
  .contact {
    position: absolute; left: 36px; bottom: 20px;
    font-family: "Lato", sans-serif; color: var(--ink-light);
  }
  .contact .name {
    font-family: "Montserrat", sans-serif; font-weight: 700;
    font-size: 23px; line-height: 1.1; text-transform: uppercase; letter-spacing: .3px;
  }
  .contact .role { font-size: 12.5px; color: var(--ink-soft); margin-bottom: 6px; }
  .contact .address { font-size: 12px; line-height: 1.35; margin-bottom: 6px; color: var(--ink-soft); }
  .contact ul { list-style: none; font-size: 12px; line-height: 1.5; }
  .contact li { display: flex; align-items: center; gap: 9px; }
  .contact svg { width: 11px; height: 11px; fill: var(--ink-soft); flex: none; }
</style>
</head>
<body>
<main class="canvas">

  <section class="card card-back" aria-label="Card back">
    <p class="wordmark">Eastfield Commercial</p>
    <p class="site">www.eastfieldcommercial.example</p>
  </section>

  <section class="card card-front" aria-label="Card front">
    <svg class="shape" viewBox="0 0 540 310" preserveAspectRatio="none" aria-hidden="true">
      <path d="M0,0 L160,0 C200,100 340,165 540,160 L540,310 L0,310 Z" fill="var(--card-dark)"/>
      <path d="M160,0 C200,100 340,165 540,160" fill="none" stroke="var(--brand-red)" stroke-width="6"/>
    </svg>

    <p class="wordmark">Eastfield Commercial</p>

    <div class="contact">
      <p class="name">Anders Voll</p>
      <p class="role">Director</p>
      <p class="address">48 Alder Ridge Way,<br>Lakeview MN 55000</p>
      <ul>
        <li><svg viewBox="0 0 12 12"><path d="M2.5 1l2 2.2-1 1.3c.7 1.5 1.8 2.6 3.2 3.3l1.3-1 2.2 2-1.2 1.9C5 10.4 1.6 7 .6 2.2z"/></svg>555 203 8841</li>
        <li><svg viewBox="0 0 12 12"><path d="M3 0h6v12H3zM4 1.5v8h4v-8z"/></svg>555 287 3096</li>
        <li><svg viewBox="0 0 12 12"><path d="M0 2h12v8H0zM1 3v.4l5 3.3 5-3.3V3zM1 4.6V9h10V4.6L6 7.9z"/></svg>anders@eastfieldcommercial.example</li>
        <li><svg viewBox="0 0 12 12"><path d="M6 0a6 6 0 100 12A6 6 0 006 0zm0 1.2a4.8 4.8 0 110 9.6 4.8 4.8 0 010-9.6zM1.5 5.4h9v1.2h-9zM5.4 1.5h1.2v9H5.4z"/></svg>www.eastfieldcommercial.example</li>
      </ul>
    </div>
  </section>

</main>
</body>
</html>
```